Lawn sign for construction company

Would like this to be a very clean and high end design for luxury homes. We need a yard sign designed that includes the company logo, website, phone number and major service offerings (residential and commercial renovations and maintenance)
The company website is brackwellbuilders.com all other contact info is in the attachments
Target Market(s)
Luxury home owners and business owners
Industry/Entity Type
Construction/Home Improvement
Font styles to use
Other font styles liked:
- See company logo and other graphics included for title text fonts. All other fonts can be standard sans serif.
Colors
0054AA
0677BA
7BADD7
CADEEF
E8F1F8
Requirements
Must have
- Clean, easy to read design, would like 2 sided sign. A main sign side and back side which states “free estimates, and includes the website and phone number. Must also match the color scheme of the provided logo and other company images. Dark Navy blue primary color, gray secondary color, and orange as an accent color.
Nice to have
- 2nd sign side very simple design
Should not have
- Too many graphics limit to 1-3 colors

```html
<!DOCTYPE html>
<html lang="en">
<head>
<meta charset="utf-8">
<title>Brackwell Builders – Yard Sign</title>
<link rel="stylesheet" href="https://fonts.googleapis.com/css2?family=Montserrat:wght@400;500;600;800;900&family=Arimo:wght@400&display=swap">
<style>
  :root {
    --navy: #07076b;
    --orange: #ef7a0a;
    --grey: #6a6a6a;
    --white: #ffffff;
    --paper: #f4f4f4;
    --backdrop: #7a7a7a;
  }
  * { margin: 0; padding: 0; box-sizing: border-box; }
  html, body { width: 1200px; height: 2355px; overflow: hidden; }
  body {
    background: var(--backdrop);
    font-family: "Montserrat", sans-serif;
    position: relative;
  }
  .side-label {
    position: absolute;
    left: 100px;
    color: var(--white);
    font-family: "Arimo", sans-serif;
    font-size: 58px;
    letter-spacing: 1px;
    transform: translate(-50%, -50%) rotate(-90deg);
    white-space: nowrap;
  }
  .side-label--front { top: 743px; }
  .side-label--back { top: 1590px; }

  .sign {
    position: absolute;
    left: 210px;
    width: 860px;
    height: 687px;
    overflow: hidden;
    box-shadow: 0 18px 22px -14px rgba(0,0,0,0.45);
  }
  .sign--front { top: 400px; background: var(--white); }
  .sign--back { top: 1247px; background: var(--navy); }

  /* front */
  .front-field {
    position: absolute; left: 0; top: 0; width: 860px; height: 508px;
    background: linear-gradient(160deg, #ffffff 0%, #ececec 30%, #ffffff 48%, #e6e6e6 70%, #fafafa 100%);
  }
  .front-frame {
    position: absolute; left: 26px; top: 26px; right: 26px; height: 482px;
    border: 3px solid var(--navy); border-bottom: none;
  }
  .front-frame::after {
    content: ""; position: absolute; left: 11px; top: 11px; right: 11px; bottom: 0;
    border: 1px solid var(--navy); border-bottom: none;
  }
  .brand {
    position: absolute; left: 0; right: 0; top: 205px;
    display: flex; align-items: center; justify-content: center; gap: 22px;
  }
  .brand-dot { width: 44px; height: 44px; border-radius: 50%; background: var(--orange); }
  .brand-name {
    font-weight: 800; font-size: 54px; color: var(--navy);
    letter-spacing: 1px; text-transform: uppercase;
  }
  .services {
    position: absolute; left: 0; top: 508px; width: 860px; height: 179px;
    background: var(--navy); color: var(--white);
    display: flex; flex-direction: column; align-items: center; justify-content: center;
    font-size: 37px; line-height: 1.45; text-transform: uppercase; letter-spacing: 0.3px;
  }
  .services strong { font-weight: 800; }
  .services span { font-weight: 400; }

  /* back */
  .back-frame {
    position: absolute; left: 26px; top: 26px; right: 26px; bottom: 26px;
    border: 2px solid var(--white);
  }
  .back-frame::after {
    content: ""; position: absolute; inset: 11px; border: 1px solid var(--white);
  }
  .credential {
    position: absolute; left: 0; right: 0; top: 96px; text-align: center;
    color: var(--white); font-weight: 800; font-size: 29px; letter-spacing: 5px;
  }
  .ribbon {
    position: absolute; left: 108px; width: 652px; height: 94px;
    background: var(--white); transform: rotate(-4deg);
    display: flex; align-items: center; justify-content: center;
    color: var(--orange); font-weight: 900; letter-spacing: 1px;
  }
  .ribbon--offer { top: 168px; font-size: 62px; }
  .ribbon--phone { top: 296px; font-size: 80px; }
  .website {
    position: absolute; left: 0; right: 0; top: 466px; text-align: center;
    color: var(--white); font-weight: 500; font-size: 42px; letter-spacing: 1px;
  }
  .address {
    position: absolute; left: 0; right: 0; top: 548px; text-align: center;
    color: var(--white); font-weight: 500; font-size: 25px; line-height: 1.55;
  }
</style>
</head>
<body>
  <div class="side-label side-label--front">FRONT</div>
  <div class="side-label side-label--back">BACK</div>

  <section class="sign sign--front">
    <div class="front-field" role="img" aria-label="Soft white draped fabric texture background"></div>
    <div class="front-frame"></div>
    <div class="brand">
      <div class="brand-dot"></div>
      <div class="brand-name">Brackwell Builders</div>
    </div>
    <div class="services">
      <p><strong>Residential</strong> <span>and</span> <strong>Commercial</strong></p>
      <p><strong>Renovations</strong> <span>and</span> <strong>Maintenance</strong></p>
    </div>
  </section>

  <section class="sign sign--back">
    <div class="back-frame"></div>
    <p class="credential">LICENSED AND INSURED</p>
    <div class="ribbon ribbon--offer">FREE ESTIMATES</div>
    <div class="ribbon ribbon--phone">810-555-0142</div>
    <p class="website">www.brackwellbuilders.com</p>
    <p class="address">Corvel Road<br>Eastbrook Township, Michigan, MI, US 48000 MI</p>
  </section>
</body>
</html>
```